Collagen Tub Packaging Design for a New Brand

PLEASE DON'T SEND ANY NEW DESIGNS WE JUST HAVE TO DECIDE WITH MY PARTNERS THANKS A LOT.
I've created a very detailed document & design examples of what we like in certain designs and what we don't.

There are 3 documents:
1- Brief for the Design (please read it before designing)
2- Brand Design Examples that we like (and why we like them)
3- Die cut for the packaging design. This will be it's dimensions.

We are NOT looking for someone to micro-manage. In contrast, we want someone to help us express our ideas better with their design. Nothing I say in these briefs are there to limit the creativity of the designer, because if we knew exactly what we wanted we would do it ourselves but we trust the designer's expertise in this packaging design.

In short: We want our brand to feel premium, high-quality & trust worthy with it's design not feeling very busy or bloated. We don't have a logo source file, but you'll get the idea of what we want when you see it).

Let me know if you have any further questions, will answer each question real fast.

Thanks.

Target Market(s)

Pretty much everyone above 25+ in Turkey because nearly all of them are using are collagens so our audience is wild.

Industry/Entity Type

Collagen - Health, Wellness & Supplements

Font styles to use
Serif
Sans Serif

Colors

Designer to choose colors to be used in the design.

Requirements
Must have
• Our design should be distinct, a design style which everyone can identify from 10 meters away if they know the product. This is a MUST have for us. It's up to designer to achieve it. This can be just a simple color palette aswell.
Should not have
• It shouldn't feel bloated and very busy. Please avoid very detailed icons (as a rule of thumb, if you can make it work great)

```html
<!DOCTYPE html>
<html lang="en">
<head>
<meta charset="utf-8">
<title>Lunavie Hydrolyzed Collagen Peptides – Tub Label</title>
<link rel="stylesheet" href="https://fonts.googleapis.com/css2?family=Marcellus&family=Oswald:wght@600&family=Montserrat:wght@300;400&display=swap">
<style>
  :root {
    --page-bg: #cfcfcf;
    --label-bg: #ededed;
    --label-glow: #ffffff;
    --band-grey: #b9bcc2;
    --navy: #1f3d8c;
    --deep-blue: #173a86;
    --royal-blue: #1f6fc2;
    --sky-blue: #2f86d6;
    --soft-blue: #3b5fae;
    --cross-grey: #e3e3e3;
    --gold: #b8925c;
    --gold-light: #d9bd8f;
    --white: #ffffff;
  }
  * { margin: 0; padding: 0; box-sizing: border-box; }
  html, body { width: 1200px; height: 1200px; overflow: hidden; }
  body { background: var(--page-bg); position: relative; font-family: "Marcellus", serif; }

  .label {
    position: absolute; left: 150px; top: 32px; width: 900px; height: 1135px;
    background: radial-gradient(ellipse at 50% 45%, var(--label-glow) 0%, var(--label-bg) 75%);
    overflow: hidden;
  }
  .label-band { position: absolute; left: 0; width: 100%; height: 29px; background: var(--band-grey); }
  .label-band--top { top: 14px; }
  .label-band--bottom { top: 1078px; }

  .brand-cross { position: absolute; background: var(--cross-grey); }
  .brand-cross--vertical { left: 46px; top: 660px; width: 55px; height: 262px; }
  .brand-cross--horizontal { left: 10px; top: 752px; width: 161px; height: 84px; }

  .brand-name {
    position: absolute; left: 0; width: 900px; top: 100px; text-align: center;
    font-size: 118px; line-height: 1; color: var(--deep-blue); letter-spacing: 2px;
  }

  .product-type {
    position: absolute; left: 90px; top: 272px; font-size: 40px; color: var(--soft-blue);
  }
  .product-name { position: absolute; left: 78px; top: 318px; width: 740px; height: 130px; }
  .product-sub {
    position: absolute; left: 0; width: 900px; top: 440px; text-align: center;
    font-size: 66px; color: var(--deep-blue); letter-spacing: 2px; -webkit-text-stroke: 1.5px var(--deep-blue);
  }

  .claim-pill {
    position: absolute; left: 84px; top: 551px; width: 720px; height: 57px; border-radius: 20px;
    background: linear-gradient(90deg, var(--soft-blue) 0%, var(--royal-blue) 50%, var(--soft-blue) 100%);
    display: flex; align-items: center; justify-content: center; gap: 30px;
    color: var(--white); font-size: 28px; letter-spacing: 1px;
  }
  .benefit-list {
    position: absolute; left: 84px; top: 612px; width: 720px; display: flex; justify-content: space-between;
    font-size: 28px; color: var(--navy); padding: 0 22px;
  }
  .divider { color: var(--navy); }

  .source-illustration {
    position: absolute; left: 345px; top: 670px; width: 200px; height: 200px; border-radius: 50%;
    background: radial-gradient(circle, var(--gold-light) 0%, var(--gold) 80%);
  }

  .flavour-pill {
    position: absolute; left: 312px; top: 895px; width: 268px; height: 32px; border-radius: 16px;
    background: var(--deep-blue); color: var(--white); text-align: center;
    font-size: 22px; line-height: 32px; letter-spacing: 5px;
  }

  .nutrition { position: absolute; left: 0; top: 928px; width: 900px; height: 100px; }
  .nutrition-item { position: absolute; transform: translateX(-50%); text-align: center; }
  .nutrition-value {
    font-family: "Oswald", sans-serif; font-weight: 600; font-size: 62px; line-height: 1;
    color: var(--royal-blue); background: linear-gradient(180deg, var(--sky-blue), var(--deep-blue));
    -webkit-background-clip: text; background-clip: text; -webkit-text-fill-color: transparent;
  }
  .nutrition-unit { font-size: 32px; }
  .nutrition-label {
    font-family: "Montserrat", sans-serif; font-weight: 400; font-size: 23px; line-height: 1.2;
    color: var(--soft-blue); margin-top: 4px;
  }

  .legal-line {
    position: absolute; left: 0; width: 900px; top: 1040px; text-align: center;
    font-family: "Montserrat", sans-serif; font-weight: 300; font-size: 23px; line-height: 1.2;
    color: var(--soft-blue); word-spacing: 2px;
  }
  .legal-line .divider { color: var(--soft-blue); margin: 0 28px; }
</style>
</head>
<body>
  <main class="label">
    <div class="label-band label-band--top"></div>
    <div class="brand-cross brand-cross--vertical"></div>
    <div class="brand-cross brand-cross--horizontal"></div>

    <div class="brand-name">Lunavie</div>

    <div class="product-type">hydrolyzed</div>
    <svg class="product-name" viewBox="0 0 740 130" aria-label="Collagen">
      <defs>
        <linearGradient id="headline-blue" x1="0" y1="0" x2="0" y2="1">
          <stop offset="0" stop-color="#2f86d6"/>
          <stop offset="1" stop-color="#173a86"/>
        </linearGradient>
      </defs>
      <text x="370" y="118" text-anchor="middle" textLength="730" lengthAdjust="spacingAndGlyphs"
            font-family="Marcellus, serif" font-size="148" fill="url(#headline-blue)">COLLAGEN</text>
    </svg>
    <div class="product-sub">PEPTIDES</div>

    <div class="claim-pill">
      <span>HIGH ABSORPTION</span><span>|</span><span>HIGH-QUALITY MATERIAL</span>
    </div>
    <div class="benefit-list">
      <span>SKIN</span><span class="divider">|</span>
      <span>HAIR</span><span class="divider">|</span>
      <span>JOINT</span><span class="divider">|</span>
      <span>MOOD</span><span class="divider">|</span>
      <span>FAT LOSS</span>
    </div>

    <div class="source-illustration" role="img" aria-label="Gold illustration of a bovine head inside a circle, marking the collagen source"></div>

    <div class="flavour-pill">FLAVOURLESS</div>

    <section class="nutrition">
      <div class="nutrition-item" style="left:157px"><div class="nutrition-value">0<span class="nutrition-unit">G</span></div><div class="nutrition-label">SUGAR</div></div>
      <div class="nutrition-item" style="left:280px"><div class="nutrition-value">0<span class="nutrition-unit">G</span></div><div class="nutrition-label">CARBS</div></div>
      <div class="nutrition-item" style="left:395px"><div class="nutrition-value">0<span class="nutrition-unit">G</span></div><div class="nutrition-label">FAT</div></div>
      <div class="nutrition-item" style="left:530px"><div class="nutrition-value">11<span class="nutrition-unit">G</span></div><div class="nutrition-label">PROTEIN</div></div>
      <div class="nutrition-item" style="left:708px"><div class="nutrition-value">12<span class="nutrition-unit">G</span></div><div class="nutrition-label">COLLAGEN</div></div>
    </section>

    <div class="legal-line">DIETARY SUPPLEMENT<span class="divider">|</span>NET WT 21.87 OZ (620g)</div>

    <div class="label-band label-band--bottom"></div>
  </main>
</body>
</html>
```